Online-Marketing Material für Recruiting-Plattform
Zielgruppe
Recruiting-Plattform für Physiotherapeuten. Wir sind Vermittler.
Aufgabenstellung
Ich benötige ein 2er Set aus Social-Media-Templates, das wir als Basis für Recruiting-Ads nutzen können.
Variante 1: (1080 x 1350) mit jeweils 285 Pixel Safe Space oben und unten (hier keine wichtigen Elemente).
Wichtig: Es handelt sich um ein Template. Daher muss es mit verschiedenen Elementen und Fotos funktionieren.
Die Elemente werden später durch variable Inhalte gesetzt. Ziel ist es, ein möglichst flexibles Format zu schaffen,
das mit unterschiedlichen Inhalten funktioniert.
Bitte orientiere dich am Grunddesign der Website therapunkt.de
Elemente und zugehörige Beispiele sind
1. Foto in querformat | Beispiel als Download)
2. Jobtitel als Headline | (Physiotherapeut (m/w/d)
3. Subtitle | Werde Teil eines wachsenden Teams
4. Arbeitszeitmodell | Vollzeit, Teilzeit
3. Ort | Hannover
4. 3 x Highlights | 1. Betriebliche Krankenversicherung 2. Tretlux 3. Gehalt bis zu 4.500 EUR
(Die Highlight variieren thematisch, daher hier bitte nur mit thematisch-neutralen Icons arbeiten.
5. Logo des Arbeitgebers (lusen) auf weiß
Variante 2 mit Foto in hochformat

```html
<!DOCTYPE html>
<html lang="de">
<head>
<meta charset="utf-8">
<title>Therapunkt – Recruiting-Templates Physiotherapeut</title>
<link rel="stylesheet" href="https://fonts.googleapis.com/css2?family=Roboto+Slab:wght@700;800&family=Montserrat:wght@600&family=Poppins:wght@600;700&display=swap">
<style>
  :root {
    --stage: #464646;
    --paper: #ffffff;
    --paper-grey: #f0f0f0;
    --ink: #0b3a48;
    --pink: #d4547c;
    --blue: #5b93c4;
    --brand-dark: #2b2b2b;
  }
  * { box-sizing: border-box; margin: 0; padding: 0; }
  html, body { width: 1200px; height: 1117px; overflow: hidden; }
  body { background: var(--stage); position: relative; font-family: "Poppins", sans-serif; }

  .ad {
    position: absolute; top: 233px; width: 521px; height: 651px;
    background: var(--paper); overflow: hidden;
    box-shadow: 0 6px 18px rgba(0,0,0,.35);
  }
  .ad--landscape { left: 69px; }
  .ad--portrait { left: 610px; }

  .ad__lower { position: absolute; left: 0; top: 359px; width: 100%; height: 292px; background: var(--paper-grey); }
  .ad__shapes { position: absolute; inset: 0; width: 521px; height: 651px; }

  .brand { position: absolute; left: 36px; top: 160px; display: flex; align-items: center; gap: 8px; }
  .brand__dot { width: 18px; height: 18px; border-radius: 50%; background: var(--pink); }
  .brand__name { font-family: "Roboto Slab", serif; font-weight: 700; font-size: 21px; line-height: 24px; color: var(--brand-dark); letter-spacing: .5px; }

  .job-title {
    position: absolute; left: 36px; top: 216px;
    font-family: "Roboto Slab", serif; font-weight: 800;
    font-size: 43px; line-height: 43px; color: var(--ink); letter-spacing: -.8px;
  }
  .subtitle {
    position: absolute; left: 41px; top: 372px;
    font-family: "Montserrat", sans-serif; font-weight: 600;
    font-size: 15.5px; line-height: 18.5px; color: var(--pink); letter-spacing: -.3px;
  }

  .highlights { position: absolute; left: 14px; top: 424px; width: 240px; height: 60px; }
  .highlight { position: absolute; top: 0; width: 92px; margin-left: -46px; text-align: center; }
  .highlight svg { display: block; margin: 0 auto; width: 28px; height: 28px; }
  .highlight__label { font-weight: 700; font-size: 8px; line-height: 9.5px; color: var(--ink); margin-top: 7px; }
  .highlight:nth-child(1) { left: 40px; }
  .highlight:nth-child(1) .highlight__label { margin-top: 11px; }
  .highlight:nth-child(2) { left: 114px; }
  .highlight:nth-child(3) { left: 195px; }
  .highlights__rule { position: absolute; top: 6px; width: 1.5px; height: 28px; background: var(--pink); }

  .photo { position: absolute; }
  .photo--landscape {
    left: 249px; top: 143px; width: 272px; height: 363px; border-radius: 30px 0 0 30px;
    background: linear-gradient(150deg, #fbf3c6 0%, #f4ecd7 35%, #e9e6df 60%, #8d8b86 85%, #4b4a48 100%);
  }
  .photo--portrait {
    left: 228px; top: 177px; width: 293px; height: 214px; border-radius: 20px 0 0 20px;
    background: linear-gradient(120deg, #5e7c86 0%, #dfe3e4 30%, #eef0f1 55%, #cfd4dc 75%, #f3f3f3 100%);
  }

  .facts {
    position: absolute; left: 266px; top: 426px; width: 255px; height: 57px;
    background: var(--pink); border-radius: 29px 0 0 29px;
    color: #fff; font-weight: 700; font-size: 12.5px; line-height: 16px;
  }
  .fact { position: absolute; left: 33px; display: flex; align-items: center; gap: 10px; white-space: nowrap; }
  .fact:nth-child(1) { top: 8px; }
  .fact:nth-child(2) { top: 32px; }
  .fact svg { width: 14px; height: 14px; }
</style>
</head>
<body>

<section class="ad ad--landscape">
  <div class="ad__lower"></div>
  <svg class="ad__shapes" viewBox="0 0 521 651" aria-hidden="true">
    <rect x="0" y="65" width="203" height="6" fill="var(--pink)"/>
    <rect x="209" y="65" width="67" height="6" fill="var(--blue)"/>
    <rect x="244" y="573" width="67" height="6" fill="var(--blue)"/>
    <rect x="317" y="573" width="204" height="6" fill="var(--pink)"/>
    <path d="M521 0 L 411 0 A 110 110 0 0 0 521 110 Z" fill="var(--pink)"/>
    <path d="M0 651 L 0 531 A 120 120 0 0 1 120 651 Z" fill="var(--blue)"/>
  </svg>

  <div class="photo photo--landscape" role="img" aria-label="Foto im Querformat: heller Behandlungsraum einer Physiotherapie-Praxis mit Liege, Fenster und Bildern an der Wand"></div>

  <div class="brand"><span class="brand__dot"></span><span class="brand__name">THERAPUNKT</span></div>
  <h1 class="job-title">Physio-<br>therapeut<br>(m/w/d)</h1>
  <p class="subtitle">Werde Teil eines<br>wachsenden Teams</p>

  <div class="highlights">
    <div class="highlight">
      <svg viewBox="0 0 28 28" fill="none" stroke="var(--blue)" stroke-width="1.6"><rect x="2" y="8" width="24" height="16" rx="3"/><path d="M10 8V5h8v3M2 15h24"/><rect x="12" y="13" width="4" height="4" rx="1"/></svg>
      <p class="highlight__label">Tretlux</p>
    </div>
    <div class="highlight">
      <svg viewBox="0 0 28 28" fill="none" stroke="var(--blue)" stroke-width="1.6"><path d="M14 1 L 22 10 A 11 11 0 1 1 6 10 Z"/><path d="M12 11h4v4h3v4h-3v4h-4v-4H9v-4h3z"/></svg>
      <p class="highlight__label">Betriebliche Krankenversicherung</p>
    </div>
    <div class="highlight">
      <svg viewBox="0 0 28 28" fill="none" stroke="var(--blue)" stroke-width="1.6"><path d="M22 14v11H3V6h14"/><path d="M8 14l5 5L26 3"/></svg>
      <p class="highlight__label">Gehalt bis zu<br>4.500 EUR</p>
    </div>
    <span class="highlights__rule" style="left:80px"></span>
    <span class="highlights__rule" style="left:157px"></span>
  </div>

  <div class="facts">
    <div class="fact"><svg viewBox="0 0 14 14" fill="none" stroke="#fff" stroke-width="1.3"><circle cx="7" cy="7" r="6"/><path d="M7 3.5V7l2.5 1.5"/></svg>Vollzeit | Teilzeit</div>
    <div class="fact"><svg viewBox="0 0 14 14" fill="none" stroke="#fff" stroke-width="1.3"><path d="M7 13s-4.5-4.5-4.5-7.5a4.5 4.5 0 0 1 9 0C11.5 8.5 7 13 7 13z"/><circle cx="7" cy="5.5" r="1.6"/></svg>Standort bei Hannover</div>
  </div>
</section>

<section class="ad ad--portrait">
  <div class="ad__lower"></div>
  <svg class="ad__shapes" viewBox="0 0 521 651" aria-hidden="true">
    <rect x="0" y="65" width="203" height="6" fill="var(--pink)"/>
    <rect x="209" y="65" width="67" height="6" fill="var(--blue)"/>
    <rect x="244" y="573" width="67" height="6" fill="var(--blue)"/>
    <rect x="317" y="573" width="204" height="6" fill="var(--pink)"/>
    <path d="M521 0 L 411 0 A 110 110 0 0 0 521 110 Z" fill="var(--pink)"/>
    <path d="M0 651 L 0 531 A 120 120 0 0 1 120 651 Z" fill="var(--blue)"/>
  </svg>

  <div class="brand"><span class="brand__dot"></span><span class="brand__name">THERAPUNKT</span></div>
  <h1 class="job-title">Physio-<br>therapeut<br>(m/w/d)</h1>
  <p class="subtitle">Werde Teil eines<br>wachsenden Teams</p>

  <div class="photo photo--portrait" role="img" aria-label="Foto: Physiotherapeutin behandelt das Bein eines älteren Patienten auf einer Therapieliege in einem hellen Raum"></div>

  <div class="highlights">
    <div class="highlight">
      <svg viewBox="0 0 28 28" fill="none" stroke="var(--blue)" stroke-width="1.6"><rect x="2" y="8" width="24" height="16" rx="3"/><path d="M10 8V5h8v3M2 15h24"/><rect x="12" y="13" width="4" height="4" rx="1"/></svg>
      <p class="highlight__label">Tretlux</p>
    </div>
    <div class="highlight">
      <svg viewBox="0 0 28 28" fill="none" stroke="var(--blue)" stroke-width="1.6"><path d="M14 1 L 22 10 A 11 11 0 1 1 6 10 Z"/><path d="M12 11h4v4h3v4h-3v4h-4v-4H9v-4h3z"/></svg>
      <p class="highlight__label">Betriebliche Krankenversicherung</p>
    </div>
    <div class="highlight">
      <svg viewBox="0 0 28 28" fill="none" stroke="var(--blue)" stroke-width="1.6"><path d="M22 14v11H3V6h14"/><path d="M8 14l5 5L26 3"/></svg>
      <p class="highlight__label">Gehalt bis zu<br>4.500 EUR</p>
    </div>
    <span class="highlights__rule" style="left:80px"></span>
    <span class="highlights__rule" style="left:157px"></span>
  </div>

  <div class="facts">
    <div class="fact"><svg viewBox="0 0 14 14" fill="none" stroke="#fff" stroke-width="1.3"><circle cx="7" cy="7" r="6"/><path d="M7 3.5V7l2.5 1.5"/></svg>Vollzeit | Teilzeit</div>
    <div class="fact"><svg viewBox="0 0 14 14" fill="none" stroke="#fff" stroke-width="1.3"><path d="M7 13s-4.5-4.5-4.5-7.5a4.5 4.5 0 0 1 9 0C11.5 8.5 7 13 7 13z"/><circle cx="7" cy="5.5" r="1.6"/></svg>Standort bei Hannover</div>
  </div>
</section>

</body>
</html>
```